Design a "healthy, happy dog and cat" cheque/check background

I am looking for a few design concepts featuring a happy healthy dog and cat, that will be used as the background of a paper cheque/check.

This will require Photoshop and stock photos.

Here is the design brief: https://files.brivontel.net/sheet/48kQmZ2xTrWvLpN7aHcYeJ5uBdFsKo9GiRtXnVw3Lz/view?share=on

Colors

Designer to choose colors to be used in the design.

Requirements
Must have
• A happy dog and cat the main focus within the "empty" central part of the cheque/check, and a complementary background for the rest of the cheque, following the design guidelines in the attached google doc.

```html
<!DOCTYPE html>
<html lang="en">
<head>
<meta charset="utf-8">
<title>Pet Cheque Designs</title>
<link rel="stylesheet" href="https://fonts.googleapis.com/css2?family=Archivo:wght@400;700&family=Source+Sans+3:wght@400&family=Share+Tech+Mono&display=swap">
<style>
  :root {
    --accent: #14b4ee;
    --ink: #1a1a1a;
    --line: #2b2b2b;
    --field: #ffffff;
    --label: #4a4a4a;
    --badge: #f4f4f4;
    --micr: #2a2a2a;
  }
  html, body { margin: 0; padding: 0; overflow: hidden; }
  body { width: 1200px; height: 1200px; background: #ffffff; position: relative; font-family: "Archivo", Arial, sans-serif; color: var(--ink); }

  .cheque { position: absolute; left: 24px; width: 1172px; height: 392px; border-right: 4px solid var(--accent); border-bottom: 5px solid var(--accent); box-sizing: content-box; overflow: hidden; }
  .cheque--one { top: 20px; }
  .cheque--two { top: 656px; }

  .cheque__photo { position: absolute; inset: 0; }
  .cheque--one .cheque__photo { background: linear-gradient(90deg, #e4e4e4 0%, #cfcdcb 30%, #d9ccc0 60%, #e2d6cb 100%); }
  .cheque--two .cheque__photo { background: linear-gradient(90deg, #e6dcd5 0%, #e2ddcc 30%, #dfe0c8 60%, #e8ecd6 100%); }

  .pet { position: absolute; }
  .pet--cat-grey { left: 64px; top: 16px; width: 480px; height: 380px; border-radius: 46% 46% 20% 20%; background: radial-gradient(ellipse at 50% 45%, rgba(150,150,152,.85) 0%, rgba(170,170,172,.6) 50%, rgba(200,200,200,0) 78%); }
  .pet--dog-golden { left: 470px; top: 30px; width: 680px; height: 380px; border-radius: 50% 40% 18% 30%; background: radial-gradient(ellipse at 50% 55%, rgba(196,140,96,.85) 0%, rgba(206,160,120,.6) 48%, rgba(220,200,180,0) 78%); }

  .pet--kitten { left: 210px; top: 206px; width: 150px; height: 190px; border-radius: 45% 45% 10% 10%; background: radial-gradient(ellipse at 50% 50%, rgba(180,174,166,.75) 0%, rgba(200,195,186,0) 75%); }
  .pet--pug { left: 344px; top: 104px; width: 170px; height: 292px; border-radius: 48% 48% 12% 12%; background: radial-gradient(ellipse at 50% 45%, rgba(214,196,168,.9) 0%, rgba(220,205,180,.5) 55%, rgba(230,220,200,0) 80%); }
  .pet--longhair-cat { left: 464px; top: 180px; width: 178px; height: 216px; border-radius: 45% 45% 10% 10%; background: radial-gradient(ellipse at 50% 50%, rgba(170,150,126,.85) 0%, rgba(190,172,150,.5) 55%, rgba(210,200,180,0) 80%); }
  .pet--husky { left: 632px; top: 44px; width: 170px; height: 352px; border-radius: 48% 48% 10% 10%; background: radial-gradient(ellipse at 50% 45%, rgba(196,188,172,.9) 0%, rgba(214,208,194,.55) 55%, rgba(225,225,210,0) 80%); }
  .pet--terrier { left: 784px; top: 132px; width: 130px; height: 264px; border-radius: 46% 46% 10% 10%; background: radial-gradient(ellipse at 50% 50%, rgba(110,92,78,.75) 0%, rgba(150,130,110,.45) 55%, rgba(200,200,180,0) 80%); }

  .t { position: absolute; white-space: nowrap; line-height: 1; }
  .title { left: 38px; top: 40px; font-size: 22px; font-weight: 700; color: #222; letter-spacing: .3px; }
  .addr { left: 38px; font-size: 20px; color: #222; }
  .addr--1 { top: 65px; }
  .addr--2 { top: 86px; }

  .number { left: 1000px; top: 30px; font-size: 26px; font-weight: 700; }
  .date-label { left: 760px; top: 92px; font-size: 19px; }
  .date-boxes { position: absolute; left: 824px; top: 70px; display: flex; gap: 3px; }
  .date-boxes span { width: 36px; height: 36px; background: var(--field); }
  .date-keys { position: absolute; left: 824px; top: 112px; display: flex; gap: 3px; font-size: 15px; }
  .date-keys span { width: 36px; text-align: center; }

  .pay-label { left: 32px; top: 170px; font-size: 15px; line-height: 14px; color: var(--label); }
  .rule { position: absolute; height: 1px; background: var(--line); }
  .rule--pay { left: 32px; top: 202px; width: 868px; }
  .tick { position: absolute; left: 900px; top: 172px; width: 1px; height: 31px; background: var(--line); }
  .dollar { left: 924px; top: 166px; font-size: 30px; }
  .amount-box { position: absolute; left: 948px; top: 154px; width: 194px; height: 48px; background: var(--field); }
  .rule--words { left: 34px; top: 256px; width: 846px; }
  .slash { position: absolute; left: 880px; top: 220px; width: 1px; height: 37px; background: var(--line); transform: skewX(-14deg); transform-origin: bottom; }
  .dollars { left: 894px; top: 232px; font-size: 16px; }

  .bank-dot { position: absolute; left: 60px; top: 290px; width: 40px; height: 40px; border-radius: 50%; background: #1a1a1a; }
  .bank { left: 130px; font-size: 19px; letter-spacing: .6px; }
  .bank--name { top: 279px; font-weight: 700; }
  .bank--street { top: 299px; }
  .bank--city { top: 318px; }

  .company { left: 786px; top: 314px; font-family: "Source Sans 3", Arial, sans-serif; font-size: 15px; }
  .memo { left: 37px; top: 364px; font-size: 13px; }
  .rule--memo { left: 34px; top: 378px; width: 530px; }
  .rule--sign { left: 660px; top: 378px; width: 416px; }

  .badge { position: absolute; left: 1138px; top: 252px; width: 28px; height: 134px; background: var(--badge); border: 1px solid #555; box-sizing: border-box; }

  .micr { position: absolute; left: 52px; font-family: "Share Tech Mono", "Courier New", monospace; font-size: 28px; letter-spacing: 5px; color: var(--micr); white-space: nowrap; line-height: 1; }
  .micr--one { top: 450px; }
  .micr--two { top: 1086px; }

  .design-label { position: absolute; right: 54px; font-family: "Source Sans 3", Arial, sans-serif; font-size: 32px; letter-spacing: 3px; color: #444; }
  .design-label--one { top: 464px; }
  .design-label--two { top: 1100px; }
  .band { position: absolute; left: 0; width: 1200px; height: 16px; background: var(--accent); }
  .band--one { top: 528px; }
  .band--two { top: 1164px; }
</style>
</head>
<body>

<section class="cheque cheque--one">
  <div class="cheque__photo" role="img" aria-label="Soft faded photo of a grey and white cat lying beside a resting golden spaniel">
    <div class="pet pet--dog-golden"></div>
    <div class="pet pet--cat-grey"></div>
  </div>
  <div class="t title">Maplecrest Cheques Personal Cheque</div>
  <div class="t addr addr--1">42 Harbourview Lane</div>
  <div class="t addr addr--2">Lakeford, Ontario L2X 4R8</div>
  <div class="t number">101</div>
  <div class="t date-label">DATE</div>
  <div class="date-boxes"><span></span><span></span><span></span><span></span><span></span><span></span><span></span><span></span></div>
  <div class="date-keys"><span>D</span><span>D</span><span>M</span><span>M</span><span>Y</span><span>Y</span><span>Y</span><span>Y</span></div>
  <div class="t pay-label">PAY TO THE<br>ORDER OF</div>
  <div class="rule rule--pay"></div>
  <div class="tick"></div>
  <div class="t dollar">$</div>
  <div class="amount-box"></div>
  <div class="rule rule--words"></div>
  <div class="slash"></div>
  <div class="t dollars">100 DOLLARS</div>
  <div class="bank-dot"></div>
  <div class="t bank bank--name">Your Financial Institution</div>
  <div class="t bank bank--street">200 Finance Avenue</div>
  <div class="t bank bank--city">Your City, Your Province A1B 2CS</div>
  <div class="t company">Optional Company Name</div>
  <div class="t memo">MEMO</div>
  <div class="rule rule--memo"></div>
  <div class="rule rule--sign"></div>
  <div class="badge"></div>
</section>
<div class="micr micr--one">⑈101⑈ ⑆12345⑉678⑆ 12345⑉6789⑈</div>
<div class="design-label design-label--one">DESIGN 1</div>
<div class="band band--one"></div>

<section class="cheque cheque--two">
  <div class="cheque__photo" role="img" aria-label="Soft faded photo of a group of pets: a kitten, a pug, a long-haired cat, a husky-type dog and a small terrier sitting together">
    <div class="pet pet--kitten"></div>
    <div class="pet pet--pug"></div>
    <div class="pet pet--longhair-cat"></div>
    <div class="pet pet--husky"></div>
    <div class="pet pet--terrier"></div>
  </div>
  <div class="t title">Maplecrest Cheques Personal Cheque</div>
  <div class="t addr addr--1">42 Harbourview Lane</div>
  <div class="t addr addr--2">Lakeford, Ontario L2X 4R8</div>
  <div class="t number">101</div>
  <div class="t date-label">DATE</div>
  <div class="date-boxes"><span></span><span></span><span></span><span></span><span></span><span></span><span></span><span></span></div>
  <div class="date-keys"><span>D</span><span>D</span><span>M</span><span>M</span><span>Y</span><span>Y</span><span>Y</span><span>Y</span></div>
  <div class="t pay-label">PAY TO THE<br>ORDER OF</div>
  <div class="rule rule--pay"></div>
  <div class="tick"></div>
  <div class="t dollar">$</div>
  <div class="amount-box"></div>
  <div class="rule rule--words"></div>
  <div class="slash"></div>
  <div class="t dollars">100 DOLLARS</div>
  <div class="bank-dot"></div>
  <div class="t bank bank--name">Your Financial Institution</div>
  <div class="t bank bank--street">200 Finance Avenue</div>
  <div class="t bank bank--city">Your City, Your Province A1B 2CS</div>
  <div class="t company">Optional Company Name</div>
  <div class="t memo">MEMO</div>
  <div class="rule rule--memo"></div>
  <div class="rule rule--sign"></div>
  <div class="badge"></div>
</section>
<div class="micr micr--two">⑈101⑈ ⑆12345⑉678⑆ 12345⑉6789⑈</div>
<div class="design-label design-label--two">DESIGN 2</div>
<div class="band band--two"></div>

</body>
</html>
```